Business Card Design Project

Use newly designed logo and tie into newly designed website
I need a new logo and website layout designed for my partner's business. This is a birthday present. His business is interior painting, wallpapering and design. He also has access to a wide variety of products including carpet, fabrics, furniture, wallpaper, tile, countertops, etc. I have attached some screen shots of his website for reference. He is a one man shop and has a stellar reputation with his customers. He is on-time, very tidy, excellent with animals, and always finishes on time and on budget. There are no restrictions on colors or fonts. The logo needs to work well with the website, business cards and printed materials. The website needs to flow content for device size so it looks just as good on a cell phone or tablet as it does on a desktop computer. Whatever the heck that's called!Thanks. I am looking forward to seeing everyone's ideas.
Updates
Hi Designers,
We've reopened this project as our logo design project has just completed.
Please refer to the uploaded files and make use of either Horizontal or Vertical versions of the logo depending on what you think is suitable for your design proposals.
We look forward to your creative submissions!
Target Market(s)
Consumers looking to improve the interior environment of their homes by updating wall paint or paper, flooring (either carpet, tile, or hardwoods), counter tops, window treatments, etc. Clients tend to be more upper middle class and have certain taste levels and expectations. New logo, website and business card should align to meet those levels.
Industry/Entity Type
Cell Phone
Look and feel
Each slider illustrates characteristics of the customer's brand and the style your logo design should communicate.

```html
<!DOCTYPE html>
<html lang="en">
<head>
<meta charset="utf-8">
<title>Verdano Interior Design – Business Card</title>
<link href="https://fonts.googleapis.com/css2?family=Arimo:wght@400;700&display=swap" rel="stylesheet">
<style>
  :root {
    --stage: #e6e6e6;
    --green-dark: #5b8720;
    --green-light: #86b043;
    --brand: #5f8a1f;
    --white: #ffffff;
    --ink: #444444;
    --icon: #666666;
    --rule: #dddddd;
    --service-text: #f4f8ec;
  }
  html, body {
    margin: 0;
    width: 1200px;
    height: 1000px;
    overflow: hidden;
    background: var(--stage);
    font-family: "Arimo", Arial, sans-serif;
  }
  .card {
    position: absolute;
    left: 100px;
    top: 214px;
    width: 1000px;
    height: 571px;
    border-radius: 6px;
    overflow: hidden;
    background: linear-gradient(135deg, var(--green-dark) 0%, var(--green-light) 100%);
    box-shadow: 0 14px 40px rgba(0,0,0,0.18);
  }
  .card-panel { position: absolute; inset: 0; }
  .brand {
    position: absolute;
    left: 48px;
    top: 146px;
    display: flex;
    align-items: center;
    gap: 18px;
    color: var(--brand);
  }
  .brand-dot {
    width: 34px; height: 34px;
    border-radius: 50%;
    background: var(--brand);
    flex: none;
  }
  .brand-name {
    font-size: 30px;
    line-height: 36px;
    font-weight: 400;
    letter-spacing: 1px;
  }
  .brand-name span { display: block; }
  .brand-rule {
    position: absolute;
    left: 0; top: 262px;
    width: 440px; height: 1px;
    background: var(--rule);
  }
  .contact {
    position: absolute;
    left: 48px;
    top: 290px;
    margin: 0; padding: 0;
    list-style: none;
    color: var(--ink);
    font-size: 20px;
  }
  .contact li {
    display: flex;
    align-items: center;
    gap: 14px;
    height: 40px;
  }
  .contact svg { width: 18px; height: 18px; fill: var(--icon); flex: none; }
  .services {
    position: absolute;
    left: 700px;
    top: 92px;
    width: 260px;
    color: var(--service-text);
  }
  .services-title {
    margin: 0;
    font-size: 30px;
    font-weight: 400;
    color: var(--white);
    letter-spacing: 1px;
    padding-bottom: 12px;
    border-bottom: 1px solid rgba(255,255,255,0.55);
  }
  .services-list {
    list-style: none;
    margin: 14px 0 0;
    padding: 0;
    font-size: 16px;
  }
  .services-list li {
    display: flex;
    align-items: center;
    gap: 12px;
    height: 28px;
  }
  .services-list svg { width: 12px; height: 12px; flex: none; }
</style>
</head>
<body>
  <article class="card" aria-label="Verdano Interior Design business card">
    <svg class="card-panel" viewBox="0 0 1000 571" aria-hidden="true">
      <path d="M0 80 H330 Q372 80 388 118 L565 470 Q585 520 530 520 H0 Z" fill="#ffffff"/>
    </svg>

    <div class="brand">
      <span class="brand-dot"></span>
      <span class="brand-name"><span>VERDANO</span><span>INTERIOR DESIGN</span></span>
    </div>
    <div class="brand-rule"></div>

    <ul class="contact">
      <li>
        <svg viewBox="0 0 24 24"><path d="M12 2a7 7 0 0 0-7 7c0 5 7 13 7 13s7-8 7-13a7 7 0 0 0-7-7zm0 9.5A2.5 2.5 0 1 1 12 6.5a2.5 2.5 0 0 1 0 5z"/></svg>
        2480 W Linden Ct Ashford, KS 66120
      </li>
      <li>
        <svg viewBox="0 0 24 24"><path d="M6.6 10.8a15 15 0 0 0 6.6 6.6l2.2-2.2a1 1 0 0 1 1-.25 11.4 11.4 0 0 0 3.6.57 1 1 0 0 1 1 1V20a1 1 0 0 1-1 1A17 17 0 0 1 3 4a1 1 0 0 1 1-1h3.5a1 1 0 0 1 1 1c0 1.25.2 2.45.57 3.57a1 1 0 0 1-.25 1z"/></svg>
        (555) 204-3187
      </li>
      <li>
        <svg viewBox="0 0 24 24"><path d="M12 2a10 10 0 1 0 0 20 10 10 0 0 0 0-20zm6.9 6h-2.9a15.6 15.6 0 0 0-1.4-3.6A8 8 0 0 1 18.9 8zM12 4c.8 1.2 1.5 2.5 1.9 4h-3.8c.4-1.5 1.1-2.8 1.9-4zM4.3 14a8 8 0 0 1 0-4h3.4a16.5 16.5 0 0 0 0 4zm.8 2h2.9c.3 1.3.8 2.5 1.4 3.6A8 8 0 0 1 5.1 16zM8 8H5.1a8 8 0 0 1 4.3-3.6C8.8 5.5 8.3 6.7 8 8zm4 12c-.8-1.2-1.5-2.5-1.9-4h3.8c-.4 1.5-1.1 2.8-1.9 4zm2.3-6H9.7a14.7 14.7 0 0 1 0-4h4.6a14.7 14.7 0 0 1 0 4zm.3 5.6c.6-1.1 1.1-2.3 1.4-3.6h2.9a8 8 0 0 1-4.3 3.6zM16.3 14a16.5 16.5 0 0 0 0-4h3.4a8 8 0 0 1 0 4z"/></svg>
        www.verdanodesigns.com
      </li>
    </ul>

    <section class="services">
      <h2 class="services-title">SERVICES</h2>
      <ul class="services-list">
        <li><svg viewBox="0 0 12 12"><path d="M1 6.5 4.5 10 11 2" stroke="#fff" stroke-width="2" fill="none"/></svg>Carpet Installation</li>
        <li><svg viewBox="0 0 12 12"><path d="M1 6.5 4.5 10 11 2" stroke="#fff" stroke-width="2" fill="none"/></svg>Countertops</li>
        <li><svg viewBox="0 0 12 12"><path d="M1 6.5 4.5 10 11 2" stroke="#fff" stroke-width="2" fill="none"/></svg>Flooring</li>
        <li><svg viewBox="0 0 12 12"><path d="M1 6.5 4.5 10 11 2" stroke="#fff" stroke-width="2" fill="none"/></svg>Furniture Sales</li>
        <li><svg viewBox="0 0 12 12"><path d="M1 6.5 4.5 10 11 2" stroke="#fff" stroke-width="2" fill="none"/></svg>Hardwood Floor Repair</li>
        <li><svg viewBox="0 0 12 12"><path d="M1 6.5 4.5 10 11 2" stroke="#fff" stroke-width="2" fill="none"/></svg>Interior Designers</li>
        <li><svg viewBox="0 0 12 12"><path d="M1 6.5 4.5 10 11 2" stroke="#fff" stroke-width="2" fill="none"/></svg>Lighting</li>
        <li><svg viewBox="0 0 12 12"><path d="M1 6.5 4.5 10 11 2" stroke="#fff" stroke-width="2" fill="none"/></svg>Marble &amp; Granite</li>
        <li><svg viewBox="0 0 12 12"><path d="M1 6.5 4.5 10 11 2" stroke="#fff" stroke-width="2" fill="none"/></svg>Interior Painters</li>
        <li><svg viewBox="0 0 12 12"><path d="M1 6.5 4.5 10 11 2" stroke="#fff" stroke-width="2" fill="none"/></svg>Upholstery</li>
        <li><svg viewBox="0 0 12 12"><path d="M1 6.5 4.5 10 11 2" stroke="#fff" stroke-width="2" fill="none"/></svg>Wallpaper Removal</li>
        <li><svg viewBox="0 0 12 12"><path d="M1 6.5 4.5 10 11 2" stroke="#fff" stroke-width="2" fill="none"/></svg>Wallpaper</li>
        <li><svg viewBox="0 0 12 12"><path d="M1 6.5 4.5 10 11 2" stroke="#fff" stroke-width="2" fill="none"/></svg>Window Treatments</li>
      </ul>
    </section>
  </article>
</body>
</html>
```